Online Art Gallery & Art Management Firm looking for a business card

I'm launching an online art gallery (paintings, photography, drawings, furniture, books, ...) where people can buy all types of art. It's a platform where young and unknown artists can showcase their oeuvre.

Additionally, the venture will act as my advising company for artists. I help them out with their business side of life and become their representative.

The company name: The Velvet Parlour
Logo is attached

I'm looking for something very classy and upmarket.
Updates

Reason: Logo wasn't finished yet...

The design should include the following information: - Name: Pieter Vandomme - Title: Founder - Mobile: +32 (0) 486 514 362 - E-mail: pieter@velvet-parlour.example - Website www.velvet-parlour.example I prefer the have the logo (without website) on the one side and the information on the other. Best regards Pieter

Target Market(s)

Art buyers / art dealers / artists / middle class / upmarket /

Industry/Entity Type

Artists

Colors

Designer to choose colors to be used in the design.

Requirements
Must have
• Must communicate credibility, trust and integrity
Nice to have
• Something classy, chique
Should not have
• Nothing to artistic or creative

```html
<!DOCTYPE html>
<html lang="en">
<head>
<meta charset="utf-8">
<title>The Velvet Parlour — Business Card</title>
<link href="https://fonts.googleapis.com/css2?family=Exo+2:wght@200;400&family=Arimo:wght@700&display=swap" rel="stylesheet">
<style>
  :root {
    --backdrop: #3b3038;
    --card: #ffffff;
    --ink: #111111;
    --muted: #7a7a7a;
    --band: #0c0c0c;
    --band-text: #e6e6e6;
  }
  * { margin: 0; padding: 0; box-sizing: border-box; }
  html, body { width: 1200px; height: 800px; overflow: hidden; }
  body {
    background: var(--backdrop);
    display: flex;
    align-items: center;
    justify-content: center;
    gap: 40px;
  }
  .card {
    position: relative;
    width: 540px;
    height: 309px;
    background: var(--card);
    overflow: hidden;
    box-shadow: 0 10px 30px rgba(0,0,0,0.35);
  }
  .wordmark {
    font-family: "Exo 2", sans-serif;
    font-weight: 200;
    text-transform: uppercase;
    color: var(--ink);
    white-space: nowrap;
  }
  .card-front .wordmark {
    position: absolute;
    top: 50%;
    left: 50%;
    transform: translate(-50%, -50%);
    font-size: 26px;
    letter-spacing: 0.22em;
  }
  .card-back .wordmark {
    position: absolute;
    top: 96px;
    right: 34px;
    font-size: 19px;
    letter-spacing: 0.2em;
  }
  .contact {
    position: absolute;
    left: 34px;
    top: 120px;
  }
  .contact-name {
    font-family: "Exo 2", sans-serif;
    font-weight: 400;
    font-size: 26px;
    color: var(--ink);
    line-height: 1.1;
  }
  .contact-title {
    font-family: "Exo 2", sans-serif;
    font-weight: 400;
    font-size: 18px;
    color: var(--muted);
    margin-bottom: 10px;
  }
  .contact-line {
    display: flex;
    align-items: center;
    gap: 9px;
    font-family: "Arimo", sans-serif;
    font-weight: 700;
    font-size: 13px;
    color: var(--ink);
    line-height: 20px;
  }
  .contact-line svg { width: 12px; height: 12px; fill: var(--ink); flex: none; }
  .footer-band {
    position: absolute;
    left: 0;
    bottom: 0;
    width: 540px;
    height: 64px;
  }
  .footer-band svg { position: absolute; inset: 0; fill: var(--band); }
  .footer-url {
    position: absolute;
    left: 0;
    right: 0;
    bottom: 0;
    height: 52px;
    line-height: 52px;
    text-align: center;
    font-family: "Exo 2", sans-serif;
    font-weight: 400;
    font-size: 14px;
    letter-spacing: 0.04em;
    color: var(--band-text);
  }
</style>
</head>
<body>
  <section class="card card-back" aria-label="Business card, information side">
    <div class="wordmark">The Velvet Parlour</div>
    <div class="contact">
      <div class="contact-name">Pieter Vandomme</div>
      <div class="contact-title">Founder</div>
      <div class="contact-line">
        <svg viewBox="0 0 24 24" aria-hidden="true"><path d="M6.6 10.8c1.4 2.8 3.8 5.1 6.6 6.6l2.2-2.2c.3-.3.7-.4 1-.2 1.1.4 2.3.6 3.6.6.6 0 1 .4 1 1V20c0 .6-.4 1-1 1C10.6 21 3 13.4 3 4c0-.6.4-1 1-1h3.5c.6 0 1 .4 1 1 0 1.3.2 2.5.6 3.6.1.3 0 .7-.2 1L6.6 10.8z"/></svg>
        <span>+32 (0) 486 514 362</span>
      </div>
      <div class="contact-line">
        <svg viewBox="0 0 24 24" aria-hidden="true"><path d="M2 5h20v14H2V5zm2 2v.5l8 5 8-5V7H4zm0 2.9V17h16V9.9l-8 5-8-5z"/></svg>
        <span>pieter@velvet-parlour.example</span>
      </div>
    </div>
    <div class="footer-band">
      <svg viewBox="0 0 540 64" aria-hidden="true"><path d="M0 12H404V0H424L432 12H540V64H0Z"/></svg>
      <div class="footer-url">www.velvet-parlour.example</div>
    </div>
  </section>

  <section class="card card-front" aria-label="Business card, logo side">
    <div class="wordmark">The Velvet Parlour</div>
  </section>
</body>
</html>
```